Let's help people Orlanta with better hearing!

I need a business card for my private practice. I am a Dr. of Audiology and focus on hearing and tinnitus (ringing in the ears) treatment. My practice is named "Orlanta Hearing and Tinnitus Solutions". I want to communicate the idea of improved quality of life utilizing a natural color pallet Love the color turquoise as an accent. Want a professional look, while eye catching. I'm open to nontraditional design aesthetic. Something to get excited about and motivate people to improve their lives!

```html
<!DOCTYPE html>
<html lang="en">
<head>
<meta charset="utf-8">
<title>Orlanta Hearing and Tinnitus Solutions – Business Card Designs</title>
<link rel="stylesheet" href="https://fonts.googleapis.com/css2?family=Questrial&family=Open+Sans:wght@400;700&display=swap">
<style>
  :root {
    --bg: #3a2f2a;
    --card: #ffffff;
    --band: #cfe6f8;
    --band-strong: #74c0ec;
    --blue: #1c7cc4;
    --blue-deep: #1a6fb8;
    --grey: #8a8a8a;
    --ink: #444444;
    --accent-mark: #e8433a;
    --label: #ffffff;
  }
  * { box-sizing: border-box; margin: 0; padding: 0; }
  html, body { width: 1200px; height: 900px; overflow: hidden; }
  body { background: var(--bg); font-family: "Questrial", sans-serif; position: relative; }

  .design-label {
    position: absolute; color: var(--label);
    font-family: "Open Sans", sans-serif; font-weight: 700; font-size: 42px;
  }
  .card {
    position: absolute; background: var(--card); overflow: hidden;
    box-shadow: 0 6px 16px rgba(0,0,0,.35);
  }

  /* Contact side */
  .card--front { width: 250px; height: 390px; }
  .name-band {
    position: absolute; left: 72px; top: 14px; width: 166px; height: 30px;
    background: var(--band); text-align: center; line-height: 30px;
    font-size: 15px; color: var(--ink); font-weight: 700; font-family: "Open Sans", sans-serif;
  }
  .designation {
    position: absolute; left: 72px; top: 48px; width: 166px; text-align: center;
    font-size: 11px; color: var(--ink);
  }
  .brand { position: absolute; display: flex; align-items: center; gap: 12px; }
  .brand__dot { width: 34px; height: 34px; border-radius: 50%; background: var(--band-strong); flex: none; }
  .brand__name {
    color: var(--grey); font-size: 19px; line-height: 1.05; letter-spacing: 1px; text-transform: uppercase;
  }
  .card--front .brand { left: 28px; top: 90px; }
  .divider { position: absolute; left: 0; right: 0; top: 188px; border-top: 1px solid #e4e4e4; }
  .contact-list { position: absolute; left: 0; top: 196px; width: 250px; list-style: none; }
  .contact-list li {
    display: flex; align-items: center; gap: 22px; height: 32px; margin-bottom: 6px;
    background: var(--band); padding-left: 12px; font-size: 11px; color: var(--ink);
    font-family: "Open Sans", sans-serif; width: 236px; white-space: nowrap;
  }
  .contact-list svg { width: 16px; height: 16px; flex: none; fill: var(--blue); }

  /* Back, design 1 */
  .card--back-framed { width: 420px; height: 270px; }
  .frame { position: absolute; inset: 12px; border: 4px solid var(--band-strong); }
  .card--back-framed .brand { left: 120px; top: 60px; }
  .card--back-framed .brand__name { font-size: 28px; }
  .card--back-framed .brand__dot { width: 48px; height: 48px; }
  .tagline-light {
    position: absolute; left: 0; right: 0; top: 176px; text-align: center;
    color: var(--blue); font-size: 19px; font-family: "Open Sans", sans-serif;
  }

  /* Back, design 2 */
  .card--back-banded { width: 250px; height: 390px; background: var(--band-strong); }
  .mark-square {
    position: absolute; left: 97px; top: 27px; width: 56px; height: 56px;
    background: var(--accent-mark);
  }
  .logo-band { position: absolute; left: 0; right: 0; top: 110px; height: 115px; background: var(--card); }
  .card--back-banded .brand { left: 24px; top: 140px; }
  .tagline-bold {
    position: absolute; left: 0; right: 0; top: 255px; text-align: center;
    color: var(--blue-deep); font-family: "Open Sans", sans-serif; font-weight: 700;
    font-size: 21px; line-height: 1.3;
  }
</style>
</head>
<body>

<!-- Design 1 -->
<div class="design-label" style="left:90px; top:235px;">Design 1</div>

<section class="card card--front" style="left:330px; top:30px;">
  <div class="name-band">Name</div>
  <div class="designation">Designation</div>
  <div class="brand"><span class="brand__dot"></span><span class="brand__name">Clearwave<br>Hearing<br>Centre</span></div>
  <div class="divider"></div>
  <ul class="contact-list">
    <li><svg viewBox="0 0 16 16"><path d="M4 1h8v14H4z M5.5 2.5v11h5v-11z" fill-rule="evenodd"/></svg>+1 555 014 2290</li>
    <li><svg viewBox="0 0 16 16"><path d="M1 3h14v10H1z"/><path d="M1 3l7 6 7-6" fill="none" stroke="#fff" stroke-width="1.2"/></svg>info@orlantahearing.com</li>
    <li><svg viewBox="0 0 16 16"><circle cx="8" cy="8" r="7"/><path d="M1 8h14M8 1c3 3 3 11 0 14M8 1c-3 3-3 11 0 14" fill="none" stroke="#fff" stroke-width="1"/></svg>www.orlantahearing.com</li>
    <li><svg viewBox="0 0 16 16"><path d="M8 1a5 5 0 0 1 5 5c0 4-5 9-5 9S3 10 3 6a5 5 0 0 1 5-5z"/><circle cx="8" cy="6" r="2" fill="#fff"/></svg>48 Maple Lane, Brookfield</li>
  </ul>
</section>

<section class="card card--back-framed" style="left:640px; top:80px;">
  <div class="frame"></div>
  <div class="brand"><span class="brand__dot"></span><span class="brand__name">Clearwave<br>Hearing<br>Centre</span></div>
  <p class="tagline-light">Orlanta Hearing and Tinnitus Solutions</p>
</section>

<!-- Design 2 -->
<div class="design-label" style="left:65px; top:770px;">Design 2</div>

<section class="card card--front" style="left:290px; top:480px;">
  <div class="name-band">Name</div>
  <div class="designation">Designation</div>
  <div class="brand"><span class="brand__dot"></span><span class="brand__name">Clearwave<br>Hearing<br>Centre</span></div>
  <div class="divider"></div>
  <ul class="contact-list">
    <li><svg viewBox="0 0 16 16"><path d="M4 1h8v14H4z M5.5 2.5v11h5v-11z" fill-rule="evenodd"/></svg>+1 555 014 2290</li>
    <li><svg viewBox="0 0 16 16"><path d="M1 3h14v10H1z"/><path d="M1 3l7 6 7-6" fill="none" stroke="#fff" stroke-width="1.2"/></svg>info@orlantahearing.com</li>
    <li><svg viewBox="0 0 16 16"><circle cx="8" cy="8" r="7"/><path d="M1 8h14M8 1c3 3 3 11 0 14M8 1c-3 3-3 11 0 14" fill="none" stroke="#fff" stroke-width="1"/></svg>www.orlantahearing.com</li>
    <li><svg viewBox="0 0 16 16"><path d="M8 1a5 5 0 0 1 5 5c0 4-5 9-5 9S3 10 3 6a5 5 0 0 1 5-5z"/><circle cx="8" cy="6" r="2" fill="#fff"/></svg>48 Maple Lane, Brookfield</li>
  </ul>
</section>

<section class="card card--back-banded" style="left:660px; top:470px;">
  <div class="mark-square" role="img" aria-label="Health emblem area"></div>
  <div class="logo-band"></div>
  <div class="brand"><span class="brand__dot"></span><span class="brand__name">Clearwave<br>Hearing<br>Centre</span></div>
  <p class="tagline-bold">Orlanta Hearing<br>and<br>Tinnitus Solutions</p>
</section>

</body>
</html>
```